Icons for Workspaces for a financial CRM

We need several icons to indicate personal workspaces for different type of user(s) of our SaaS-based CRM.
We offer a front- and middle-office management software for the alternative assets industry - private equity, hedge funds, real estate, institutional investors, etc - thourgh our proprietary software called Velquor. The company's main office is in Boston.
The workspaces in question represent personalized Home pages, based on the user persona - there is a workspace for Investor Relations people, another for Deal Management people, etc. There is also a "My Home" workspace where the user can arrange their own informatation. One user can have access to sevaral workspaces, they are not limited to just one.
The buttons that will point the user the workspaces, will be placed on top left position of the screen, one under the other, as a list. The icons will be coupled with text.
Here is the list of all workspaces for which we need icons - a total of 8 icons (with explanations):
• My Home
(personalized home workspace for the logged in user)
• Fundraising
Raising money for a fund.
• Investor Relations
The management of existing client relationships
• Deal Management
The management of new investments
• Portfolio Management
The management of existing investments
• Research Management
The gathering of information about the market, industry trends, innovations, etc.
• Resource Management
The management of people resources
• Portal Management
Managing of user accounts for our investor portal. This is setting up new users, editing existing users, and deactivating prior users.
The default colors of the Velquor application are light-blue and light-grey, but we also provide different skins, so it will be good to see a couple of versions, in different colors.
Size - 32 x 32 pixels
Target Market(s)
People who work in the financial industry.
Industry/Entity Type
Financial

```html
<!DOCTYPE html>
<html lang="en">
<head>
<meta charset="utf-8">
<title>Velquor Workspace Navigation – Skins</title>
<link href="https://fonts.googleapis.com/css2?family=Arimo:wght@400;700&display=swap" rel="stylesheet">
<style>
  :root {
    --page-bg: #1f1f1f;
    --page-line: #262626;
    --panel-border: #050505;
    --content-bg: #f1f1f1;
    --heading: #4a4a4a;
    --body-text: #4f4f4f;
    --nav-text: #ffffff;

    --sky-bg: #66b6ef;
    --sky-line: #4d9fdc;
    --sky-icon: #0e2a4a;

    --forest-bg: #277f0e;
    --forest-line: #1b5a09;
    --forest-icon: #0c2406;

    --charcoal-bg: #282828;
    --charcoal-line: #1a1a1a;
    --charcoal-icon: #7c7c7c;
  }
  * { box-sizing: border-box; margin: 0; padding: 0; }
  html, body {
    width: 1200px; height: 1200px; overflow: hidden;
  }
  body {
    position: relative;
    background-color: var(--page-bg);
    background-image:
      repeating-linear-gradient(0deg, var(--page-line) 0 1px, transparent 1px 3px),
      repeating-linear-gradient(90deg, var(--page-line) 0 1px, transparent 1px 3px);
    font-family: "Arimo", Arial, sans-serif;
  }
  .icon-library { position: absolute; width: 0; height: 0; overflow: hidden; }

  .workspace-panel {
    position: absolute;
    width: 550px; height: 550px;
    border: 1px solid var(--panel-border);
    display: flex;
    overflow: hidden;
    background: var(--content-bg);
  }
  .panel-sky { left: 33px; top: 33px; --nav-bg: var(--sky-bg); --nav-line: var(--sky-line); --icon: var(--sky-icon); }
  .panel-forest { left: 616px; top: 33px; --nav-bg: var(--forest-bg); --nav-line: var(--forest-line); --icon: var(--forest-icon); }
  .panel-charcoal { left: 33px; top: 616px; --nav-bg: var(--charcoal-bg); --nav-line: var(--charcoal-line); --icon: var(--charcoal-icon); }

  .workspace-nav {
    flex: 0 0 231px;
    background: var(--nav-bg);
    border-right: 1px solid var(--panel-border);
    list-style: none;
    position: relative;
    z-index: 1;
  }
  .nav-item {
    height: 55px;
    display: flex; align-items: center;
    padding-left: 12px;
    border-bottom: 1px solid var(--nav-line);
    color: var(--nav-text);
    font-size: 13px; font-weight: 700;
  }
  .nav-icon {
    width: 32px; height: 32px;
    color: var(--icon);
    margin-right: 12px;
    flex: 0 0 32px;
  }

  .workspace-content {
    flex: 1;
    padding: 16px 0 0 21px;
    overflow: hidden;
    box-shadow: inset 6px 0 6px -4px rgba(0,0,0,0.25);
  }
  .content-title {
    font-size: 19px; font-weight: 700;
    color: var(--heading);
    margin-bottom: 11px;
  }
  .content-text {
    width: 340px;
    font-size: 13.2px; line-height: 23px;
    color: var(--body-text);
    margin-bottom: 23px;
  }
</style>
</head>
<body>

<svg class="icon-library" aria-hidden="true">
  <defs>
    <symbol id="icon-home" viewBox="0 0 32 32">
      <path fill="currentColor" d="M16 2 L1 15 L4 15 L4 30 L13 30 L13 21 L19 21 L19 30 L28 30 L28 15 L31 15 L24 9 L24 4 L21 4 L21 6.5 Z"/>
      <rect x="14" y="10" width="4" height="4" fill="var(--nav-bg)"/>
    </symbol>
    <symbol id="icon-fundraising" viewBox="0 0 32 32">
      <g fill="currentColor">
        <rect x="1" y="14" width="9" height="3" rx="1"/><rect x="1" y="18" width="9" height="3" rx="1"/>
        <rect x="1" y="22" width="9" height="3" rx="1"/><rect x="1" y="26" width="9" height="3" rx="1"/>
        <rect x="11" y="6" width="10" height="3" rx="1"/><rect x="11" y="10" width="10" height="3" rx="1"/>
        <rect x="11" y="14" width="10" height="3" rx="1"/><rect x="11" y="18" width="10" height="3" rx="1"/>
        <rect x="11" y="22" width="10" height="3" rx="1"/><rect x="11" y="26" width="10" height="3" rx="1"/>
        <rect x="22" y="18" width="9" height="3" rx="1"/><rect x="22" y="22" width="9" height="3" rx="1"/>
        <rect x="22" y="26" width="9" height="3" rx="1"/>
      </g>
    </symbol>
    <symbol id="icon-investors" viewBox="0 0 32 32">
      <g fill="currentColor">
        <circle cx="9" cy="12" r="4.5"/><path d="M1 27 C1 20 4 18 9 18 C14 18 17 20 17 27 Z"/>
        <circle cx="23" cy="12" r="4.5"/><path d="M15 27 C15 20 18 18 23 18 C28 18 31 20 31 27 Z"/>
      </g>
    </symbol>
    <symbol id="icon-deals" viewBox="0 0 32 32">
      <g fill="none" stroke="currentColor" stroke-width="1.5">
        <rect x="1" y="7" width="15" height="22"/><rect x="16" y="3" width="15" height="22"/>
        <path d="M4 12h9M4 15h9M4 18h9M4 21h6M19 8h9M19 11h9M19 14h9M19 17h6M6 25l2 2 3-4M22 21l2 2 3-4"/>
      </g>
    </symbol>
    <symbol id="icon-portfolio" viewBox="0 0 32 32">
      <path fill="currentColor" d="M11 5 H21 V9 H31 V29 H1 V9 H11 Z M13 7 V9 H19 V7 Z"/>
      <path d="M7 9 V29 M25 9 V29" stroke="var(--nav-bg)" stroke-width="1"/>
    </symbol>
    <symbol id="icon-research" viewBox="0 0 32 32">
      <path fill="currentColor" d="M14 6 A12 12 0 1 0 26 18 L14 18 Z"/>
      <path fill="currentColor" d="M17 3 A12 12 0 0 1 29 15 L17 15 Z" transform="rotate(15 17 15)"/>
    </symbol>
    <symbol id="icon-resources" viewBox="0 0 32 32">
      <g fill="none" stroke="currentColor" stroke-width="1.5">
        <path d="M10 6 V2 H30 V24 H26"/><path d="M6 10 V6 H26 V28 H22"/>
        <rect x="2" y="10" width="20" height="20"/>
      </g>
      <g fill="currentColor">
        <circle cx="12" cy="17" r="3.5"/><path d="M5 28 C5 23 8 22 12 22 C16 22 19 23 19 28 Z"/>
      </g>
    </symbol>
    <symbol id="icon-portal" viewBox="0 0 32 32">
      <rect x="1.5" y="1.5" width="29" height="29" rx="3" fill="none" stroke="currentColor" stroke-width="1.5"/>
      <g fill="currentColor">
        <rect x="5" y="5" width="10" height="10"/><rect x="17" y="5" width="10" height="10"/>
        <rect x="5" y="17" width="10" height="10"/><rect x="17" y="17" width="10" height="10"/>
      </g>
    </symbol>
  </defs>
</svg>

<section class="workspace-panel panel-sky">
  <ul class="workspace-nav">
    <li class="nav-item"><svg class="nav-icon"><use href="#icon-home"/></svg>Home</li>
    <li class="nav-item"><svg class="nav-icon"><use href="#icon-fundraising"/></svg>Fundraising</li>
    <li class="nav-item"><svg class="nav-icon"><use href="#icon-investors"/></svg>Investor Relations</li>
    <li class="nav-item"><svg class="nav-icon"><use href="#icon-deals"/></svg>Deal Management</li>
    <li class="nav-item"><svg class="nav-icon"><use href="#icon-portfolio"/></svg>Portfolio Management</li>
    <li class="nav-item"><svg class="nav-icon"><use href="#icon-research"/></svg>Research Management</li>
    <li class="nav-item"><svg class="nav-icon"><use href="#icon-resources"/></svg>Resource Management</li>
    <li class="nav-item"><svg class="nav-icon"><use href="#icon-portal"/></svg>Portal Management</li>
  </ul>
  <article class="workspace-content">
    <h2 class="content-title">Phasellus vel scelerisque eros</h2>
    <p class="content-text">Phasellus vel scelerisque eros. In vitae diam felis. Sed tincidunt nisi ut erat eleifend vitae fringilla nibh adipi scing. Phasellus et leo ante. Sed mauris massa, ultrices a sollicitudin vel, mattis id dolor. Mauris a velit lectus. Morbi ac tempus magna. Nunc lorem augue, tristique placerat vel, accumsan vitae orci. Aenean quis congue erat. Nam elit eros, laoreet vitae laoreet a, sagittis vel metus. Nulla adipiscing volutpat consequat. Integer aliquet ante et magna feugiat nec faucibus lorem eleif end. Phasellus et mi sed quam pharetra placerat ut sit amet elit. Sed nisi justo, tempus nec vestibulum ut, dignissim non orci.</p>
    <p class="content-text">Donec a nunc orci, vitae fermentum urna. Sed scelerisque accumsan odio, aliquet sollicitudin ligula tristique. Sed gravida cursus tincidunt. Sed condimentum, nunc faucibus accumsan sodales, ante augue euismod tellus, ac auctor lorem dui id purus. Fusce facilisis tellus eget nunc pulvinar non aliquam enim rutrum. Praesent massa leo, vestibulum a fermentum nec, cursus quis libero. Vestibulum ante ipsum primis in faucibus orci luctus et ultrices posuere cubilia Curae; Curabitur vel</p>
  </article>
</section>

<section class="workspace-panel panel-forest">
  <ul class="workspace-nav">
    <li class="nav-item"><svg class="nav-icon"><use href="#icon-home"/></svg>Home</li>
    <li class="nav-item"><svg class="nav-icon"><use href="#icon-fundraising"/></svg>Fundraising</li>
    <li class="nav-item"><svg class="nav-icon"><use href="#icon-investors"/></svg>Investor Relations</li>
    <li class="nav-item"><svg class="nav-icon"><use href="#icon-deals"/></svg>Deal Management</li>
    <li class="nav-item"><svg class="nav-icon"><use href="#icon-portfolio"/></svg>Portfolio Management</li>
    <li class="nav-item"><svg class="nav-icon"><use href="#icon-research"/></svg>Research Management</li>
    <li class="nav-item"><svg class="nav-icon"><use href="#icon-resources"/></svg>Resource Management</li>
    <li class="nav-item"><svg class="nav-icon"><use href="#icon-portal"/></svg>Portal Management</li>
  </ul>
  <article class="workspace-content">
    <h2 class="content-title">Phasellus vel scelerisque eros</h2>
    <p class="content-text">Phasellus vel scelerisque eros. In vitae diam felis. Sed tincidunt nisi ut erat eleifend vitae fringilla nibh adipi scing. Phasellus et leo ante. Sed mauris massa, ultrices a sollicitudin vel, mattis id dolor. Mauris a velit lectus. Morbi ac tempus magna. Nunc lorem augue, tristique placerat vel, accumsan vitae orci. Aenean quis congue erat. Nam elit eros, laoreet vitae laoreet a, sagittis vel metus. Nulla adipiscing volutpat consequat. Integer aliquet ante et magna feugiat nec faucibus lorem eleif end. Phasellus et mi sed quam pharetra placerat ut sit amet elit. Sed nisi justo, tempus nec vestibulum ut, dignissim non orci.</p>
    <p class="content-text">Donec a nunc orci, vitae fermentum urna. Sed scelerisque accumsan odio, aliquet sollicitudin ligula tristique. Sed gravida cursus tincidunt. Sed condimentum, nunc faucibus accumsan sodales, ante augue euismod tellus, ac auctor lorem dui id purus. Fusce facilisis tellus eget nunc pulvinar non aliquam enim rutrum. Praesent massa leo, vestibulum a fermentum nec, cursus quis libero. Vestibulum ante ipsum primis in faucibus orci luctus et ultrices posuere cubilia Curae; Curabitur vel</p>
  </article>
</section>

<section class="workspace-panel panel-charcoal">
  <ul class="workspace-nav">
    <li class="nav-item"><svg class="nav-icon"><use href="#icon-home"/></svg>Home</li>
    <li class="nav-item"><svg class="nav-icon"><use href="#icon-fundraising"/></svg>Fundraising</li>
    <li class="nav-item"><svg class="nav-icon"><use href="#icon-investors"/></svg>Investor Relations</li>
    <li class="nav-item"><svg class="nav-icon"><use href="#icon-deals"/></svg>Deal Management</li>
    <li class="nav-item"><svg class="nav-icon"><use href="#icon-portfolio"/></svg>Portfolio Management</li>
    <li class="nav-item"><svg class="nav-icon"><use href="#icon-research"/></svg>Research Management</li>
    <li class="nav-item"><svg class="nav-icon"><use href="#icon-resources"/></svg>Resource Management</li>
    <li class="nav-item"><svg class="nav-icon"><use href="#icon-portal"/></svg>Portal Management</li>
  </ul>
  <article class="workspace-content">
    <h2 class="content-title">Phasellus vel scelerisque eros</h2>
    <p class="content-text">Phasellus vel scelerisque eros. In vitae diam felis. Sed tincidunt nisi ut erat eleifend vitae fringilla nibh adipi scing. Phasellus et leo ante. Sed mauris massa, ultrices a sollicitudin vel, mattis id dolor. Mauris a velit lectus. Morbi ac tempus magna. Nunc lorem augue, tristique placerat vel, accumsan vitae orci. Aenean quis congue erat. Nam elit eros, laoreet vitae laoreet a, sagittis vel metus. Nulla adipiscing volutpat consequat. Integer aliquet ante et magna feugiat nec faucibus lorem eleif end. Phasellus et mi sed quam pharetra placerat ut sit amet elit. Sed nisi justo, tempus nec vestibulum ut, dignissim non orci.</p>
    <p class="content-text">Donec a nunc orci, vitae fermentum urna. Sed scelerisque accumsan odio, aliquet sollicitudin ligula tristique. Sed gravida cursus tincidunt. Sed condimentum, nunc faucibus accumsan sodales, ante augue euismod tellus, ac auctor lorem dui id purus. Fusce facilisis tellus eget nunc pulvinar non aliquam enim rutrum. Praesent massa leo, vestibulum a fermentum nec, cursus quis libero. Vestibulum ante ipsum primis in faucibus orci luctus et ultrices posuere cubilia Curae; Curabitur vel</p>
  </article>
</section>

</body>
</html>
```